business card and stationary for a auto race team
Tolland Racing
Cutting-Edge
Ross Tolland
5678 Elm Lane Fairbrook, NY, 22222
postbox@velmarsh.net
I must be able to add all information, name, address, city, state, zip code, phone number and email address.
logo can be found as winner of Tolland Racing logo design

```html
<!DOCTYPE html>
<html lang="en">
<head>
<meta charset="utf-8">
<title>Tolland Racing — Business Card</title>
<link href="https://fonts.googleapis.com/css2?family=Exo+2:wght@400;600;800&display=swap" rel="stylesheet">
<style>
  :root {
    --page: #e4e4e6;
    --card-white: #f7f7f7;
    --race-red: #d91f26;
    --deep-red: #a8141a;
    --band-black: #1c1c1e;
    --ink: #2a2a2c;
    --light-text: #ffffff;
  }
  * { margin: 0; padding: 0; box-sizing: border-box; }
  html, body {
    width: 1200px; height: 871px; overflow: hidden;
    background: var(--page);
    font-family: "Exo 2", sans-serif;
  }
  .sheet {
    width: 1200px; height: 871px;
    display: flex; align-items: center; justify-content: center; gap: 60px;
  }
  .card {
    width: 520px; height: 297px;
    border-radius: 14px; overflow: hidden;
    background: var(--card-white);
    box-shadow: 0 6px 20px rgba(0,0,0,.18);
    position: relative;
  }
  .brand {
    display: flex; align-items: center; gap: 12px;
    position: absolute; left: 50%; transform: translateX(-50%);
    white-space: nowrap;
  }
  .brand-mark { width: 18px; height: 18px; background: var(--race-red); }
  .brand-name {
    font-weight: 800; font-size: 34px; letter-spacing: 1px;
    text-transform: uppercase; color: var(--band-black);
  }
  .card-back .brand { top: 124px; }
  .card-front .brand { top: 50px; }
  .front-white { position: absolute; inset: 0 0 auto 0; height: 150px; background: var(--card-white); }
  .front-black {
    position: absolute; left: 0; right: 0; top: 150px; height: 38px;
    background: var(--band-black);
    display: flex; align-items: center; justify-content: center;
  }
  .holder-name { color: var(--race-red); font-weight: 600; font-size: 17px; }
  .front-red {
    position: absolute; left: 0; right: 0; top: 188px; bottom: 0;
    background: linear-gradient(180deg, var(--race-red), var(--deep-red));
    color: var(--light-text); font-size: 13px;
  }
  .address { text-align: center; margin-top: 24px; }
  .contact-row {
    display: flex; justify-content: space-between;
    padding: 18px 70px 0;
  }
  .contact-row b { font-weight: 600; color: var(--band-black); margin-right: 4px; }
</style>
</head>
<body>
<main class="sheet">
  <section class="card card-back">
    <div class="brand">
      <span class="brand-mark"></span>
      <span class="brand-name">Tolland Racing</span>
    </div>
  </section>

  <section class="card card-front">
    <div class="front-white"></div>
    <div class="brand">
      <span class="brand-mark"></span>
      <span class="brand-name">Tolland Racing</span>
    </div>
    <div class="front-black">
      <span class="holder-name">Ross Tolland</span>
    </div>
    <div class="front-red">
      <p class="address">5678 Elm Lane Fairbrook, NY, 22222</p>
      <div class="contact-row">
        <span class="phone"><b>P:</b>555 210 4837</span>
        <span class="email"><b>E:</b>postbox@velmarsh.net</span>
      </div>
    </div>
  </section>
</main>
</body>
</html>
```